Patient Recruitment Presentation for a Clinical Trial

We need a powerpoint designed to recruit patients for a clinical trial. We need 4 slides designed: an opening slide, two body slides, and an end slide. The opening slide should include the question, "Do you suffer from Depression?" in the middle of the screen, but other than that just include the design, graphic, or texture that you develop. The 2 body slides should allow for the title of study (please use “Depression Research Study”) to be across the top and contact information (phone number, URL) to be on the bottom of the slide, either centered or left or right justified. Whether this text (study title and contact information) is set off by a banner or shape that stretches across the entire slide or just provides a background to that text is up to you. One of the two body slides should include the attached horizontal stock image with a clear section to insert text either beside or over the top of the negative space of the image. This image should be stretch to the full width of the screen. The second body slide should include the attached vertical stock image, with a clear section to insert text beside the picture. (You can crop vertical portions of the images if needed.)

The end slide should resemble the opening slide in terms of design, yet this time includes the study title and contact information prominently displayed.

In terms of design, we’re looking for something clean and trustworthy, and even though this is medical, we don’t want any pills, test tubes, or heart rate lines. We’re trying to give people hope, so we want to earn their trust by communicating quality and excellence.

Please see the attached examples of the types of designs and layouts we like, how the images need to be treated, and places for text need to be designed.

We need the design to be 1920x1080 pixels, and we need the slides delivered as layered PSD files so we can manipulate as needed.

Thanks!

Target Market(s)

Adults in the US that are not working full time and able to participate in a research study.

Industry/Entity Type

Medical

Font styles to use
Serif
Sans Serif

Requirements
Must have
• The design must use the two images attached as specified in the brief. Other than that, I'm open to your creative interpretation.
Nice to have
• Nice clean design, clean fonts, nice color palette.
Should not have
• Images or designs relating to the medical world, no test tubes, heart rate lines, images of doctors or pills, etc.

```html
<!DOCTYPE html>
<html lang="en">
<head>
<meta charset="utf-8">
<title>Study Title</title>
<link rel="stylesheet" href="https://fonts.googleapis.com/css2?family=Roboto+Condensed:wght@300&display=swap">
<style>
  :root {
    --canvas-light: #ffffff;
    --canvas-shade: #dcdcdc;
    --ink: #1a1a1a;
    --tone-hair: #2a1f1a;
    --tone-skin-deep: #7a4a34;
    --tone-skin: #b07a5e;
    --tone-shirt: #a9c1cf;
    --seam-light: #ffffff;
    --seam-dark: #1a1a1a;
  }
  * { margin: 0; padding: 0; box-sizing: border-box; }
  html, body { width: 1200px; height: 675px; overflow: hidden; }
  body { font-family: "Roboto Condensed", "Helvetica Neue", Arial, sans-serif; font-weight: 300; color: var(--ink); }
  .slide {
    position: relative;
    width: 1200px;
    height: 675px;
    overflow: hidden;
    background: radial-gradient(ellipse 75% 80% at 62% 58%, var(--canvas-light) 55%, var(--canvas-shade) 100%);
  }
  .hex-mosaic { position: absolute; left: 0; top: 0; width: 1200px; height: 675px; }
  .study-title {
    position: absolute;
    top: 50px;
    right: 97px;
    font-size: 48px;
    font-weight: 300;
    letter-spacing: -0.5px;
    line-height: 1;
  }
  .contact {
    position: absolute;
    left: 933px;
    top: 576px;
    list-style: none;
    font-size: 25px;
    letter-spacing: -0.2px;
    line-height: 1;
    white-space: nowrap;
  }
  .contact li { display: flex; align-items: center; height: 30px; margin-bottom: 14px; }
  .contact svg { width: 18px; height: 20px; margin-right: 14px; flex: none; }
</style>
</head>
<body>
  <main class="slide">
    <svg class="hex-mosaic" viewBox="0 0 1200 675" xmlns="http://www.w3.org/2000/svg">
      <defs>
        <linearGradient id="portrait-tones" x1="0" y1="0" x2="0.6" y2="1">
          <stop offset="0" stop-color="var(--tone-hair)"/>
          <stop offset="0.3" stop-color="var(--tone-skin-deep)"/>
          <stop offset="0.55" stop-color="var(--tone-skin)"/>
          <stop offset="0.8" stop-color="var(--tone-shirt)"/>
          <stop offset="1" stop-color="var(--tone-shirt)"/>
        </linearGradient>
      </defs>
      <polygon class="portrait-area" role="img" aria-label="Portrait photo of a thoughtful woman, hand raised to her temple, cut into hexagonal tiles"
        points="0,0 555,0 580,105 775,160 820,358 675,497 718,675 0,675"
        fill="url(#portrait-tones)" stroke="var(--seam-dark)" stroke-width="2"/>
      <g class="hex-seams" fill="none" stroke-linecap="round">
        <g stroke="var(--seam-dark)" stroke-width="5">
          <path d="M200,0 L240,185 L438,243 L580,105 M438,243 L483,437 L675,497 M483,437 L340,577 L140,522 L95,323 L0,297 M95,323 L240,185 M340,577 L362,675 M140,522 L0,655"/>
        </g>
        <g stroke="var(--seam-light)" stroke-width="3">
          <path d="M200,0 L240,185 L438,243 L580,105 M438,243 L483,437 L675,497 M483,437 L340,577 L140,522 L95,323 L0,297 M95,323 L240,185 M340,577 L362,675 M140,522 L0,655"/>
        </g>
      </g>
    </svg>

    <h1 class="study-title">Study Title</h1>

    <ul class="contact">
      <li class="contact-phone">
        <svg viewBox="0 0 18 20" aria-hidden="true"><rect x="3" y="1" width="12" height="18" rx="2.2" fill="var(--ink)"/><rect x="5.2" y="3.5" width="7.6" height="11" fill="var(--canvas-light)"/><circle cx="9" cy="16.8" r="1" fill="var(--canvas-light)"/></svg>
        000-000-0000
      </li>
      <li class="contact-email">
        <svg viewBox="0 0 18 20" aria-hidden="true"><rect x="1" y="4.5" width="16" height="11" fill="var(--ink)"/><path d="M2.5 6 L9 11 L15.5 6 M2.5 14 L7 9.8 M15.5 14 L11 9.8" stroke="var(--canvas-light)" stroke-width="1.3" fill="none"/></svg>
        info.trial@example.org
      </li>
    </ul>
  </main>
</body>
</html>
```